Real Estate Company Business Cards
Renaming and Rebranding existing real estate company
Real Estate Company Business Cards - Real Estate
Creative Brief
Professional
Desmond (Hal) Pruitt, Jr
Broker, Realtor, SPS, E-Pro, BPOR,
482 Willow Bend Rd. St 23 Orange Park, Florida 32068
NC Office 910-555-0187
Fl Office 904-555-0162
hpruitt@pruittrealty.example
www.pruittrealty.example
Please dont include address in card design. These card will be printed on cotton or silk.

```html
<!DOCTYPE html>
<html lang="en">
<head>
<meta charset="utf-8">
<title>Pruitt Realty Stationery</title>
<link rel="stylesheet" href="https://fonts.googleapis.com/css2?family=Cormorant+Garamond:ital,wght@1,600&family=Open+Sans:wght@400;600&display=swap">
<style>
  :root {
    --bg: #e9ebed;
    --paper: #ffffff;
    --blue: #1f5d9c;
    --blue-light: #3d82c4;
    --grey-text: #5f6670;
    --faint: #eef1f5;
  }
  html, body { margin: 0; padding: 0; overflow: hidden; }
  body {
    width: 1200px; height: 936px; position: relative;
    background: var(--bg);
    font-family: "Open Sans", sans-serif;
  }
  .sheet { position: absolute; background: var(--paper); overflow: hidden; }
  .brand {
    font-family: "Cormorant Garamond", serif; font-style: italic; font-weight: 600;
    color: var(--blue); line-height: 1.0; display: flex; align-items: center; gap: 6px;
  }
  .brand .dot { border-radius: 50%; background: var(--blue); flex: none; }
  .brand .words span { display: block; }
  .url {
    position: absolute; color: #fff; letter-spacing: 3px; font-weight: 600;
    text-align: center; left: 0; right: 0;
  }
  .band { position: absolute; left: 0; width: 100%; }

  /* letterhead */
  .letterhead { left: 178px; top: 56px; width: 401px; height: 568px; }
  .letterhead .brand { position: absolute; left: 22px; top: 22px; font-size: 15px; }
  .letterhead .brand .dot { width: 20px; height: 20px; }
  .letterhead .contact {
    position: absolute; right: 22px; top: 22px; font-size: 5.5px; line-height: 1.55;
    color: var(--grey-text);
  }
  .letterhead .emblem {
    position: absolute; left: 130px; top: 170px; width: 130px; height: 130px;
    border-radius: 50%; background: var(--faint);
  }
  .letterhead .band { bottom: 0; height: 90px; }
  .letterhead .url { bottom: 16px; font-size: 8px; }

  /* folder */
  .folder { left: 629px; top: 38px; width: 500px; height: 596px; }
  .folder .brand { position: absolute; left: 95px; top: 262px; font-size: 30px; }
  .folder .brand .dot { width: 48px; height: 48px; }
  .folder .brand .sub { font-size: 22px; }

  /* business cards */
  .card-front { left: 38px; top: 655px; width: 203px; height: 107px; border-radius: 6px; }
  .card-front .brand { position: absolute; left: 10px; top: 9px; font-size: 10px; }
  .card-front .brand .dot { width: 12px; height: 12px; }
  .card-front .details {
    position: absolute; left: 10px; top: 44px; font-size: 4.6px; line-height: 1.45; color: var(--grey-text);
  }
  .card-front .details strong { color: var(--blue); font-weight: 600; }
  .card-front .band { bottom: 0; height: 22px; background: linear-gradient(90deg, var(--blue), var(--blue-light)); }
  .card-front .url { bottom: 7px; font-size: 5.5px; letter-spacing: 1.5px; }

  .card-back { left: 38px; top: 786px; width: 203px; height: 114px; border-radius: 6px; }
  .card-back .brand { position: absolute; left: 28px; top: 36px; font-size: 14px; }
  .card-back .brand .dot { width: 34px; height: 34px; background: var(--faint); }

  /* envelopes */
  .envelope-front { left: 266px; top: 665px; width: 414px; height: 223px; }
  .envelope-front .brand { position: absolute; left: 16px; top: 16px; font-size: 12px; }
  .envelope-front .brand .dot { width: 15px; height: 15px; }

  .envelope-back { left: 710px; top: 655px; width: 457px; height: 233px; }
  .envelope-back .band { top: 0; height: 100%; }
  .envelope-back .url { top: 70px; font-size: 8px; }
</style>
</head>
<body>

  <section class="sheet letterhead">
    <div class="brand"><span class="dot"></span><div class="words"><span>Pruitt Realty</span><span>and Property</span><span>Management Services</span></div></div>
    <div class="contact">
      NC 910-555-0187<br>FL 904-555-0162<br>hpruitt@pruittrealty.example<br>www.pruittrealty.example
    </div>
    <div class="emblem" role="img" aria-label="Faint brand emblem circle"></div>
    <svg class="band" viewBox="0 0 401 90" preserveAspectRatio="none" aria-hidden="true">
      <defs>
        <linearGradient id="lhBlue" x1="0" x2="1"><stop offset="0" stop-color="#1f5d9c"/><stop offset="1" stop-color="#3d82c4"/></linearGradient>
      </defs>
      <path d="M0 40 Q200 10 401 28 L401 90 L0 90 Z" fill="#c9d3de"/>
      <path d="M0 50 Q200 22 401 38 L401 90 L0 90 Z" fill="url(#lhBlue)"/>
    </svg>
    <div class="url">www.pruittrealty.example</div>
  </section>

  <section class="sheet folder">
    <div class="brand"><span class="dot"></span><div class="words"><span>Pruitt Realty</span><span class="sub">and Property</span><span class="sub">Management Services</span></div></div>
  </section>

  <section class="sheet card-front">
    <div class="brand"><span class="dot"></span><div class="words"><span>Pruitt Realty</span><span>and Property</span></div></div>
    <div class="details">
      <strong>Desmond (Hal) Pruitt, Jr</strong><br>
      Broker, Realtor, SPS, E-Pro, BPOR<br>
      NC Office 910-555-0187<br>
      FL Office 904-555-0162<br>
      hpruitt@pruittrealty.example
    </div>
    <div class="band"></div>
    <div class="url">www.pruittrealty.example</div>
  </section>

  <section class="sheet card-back">
    <div class="brand"><span class="dot"></span><div class="words"><span>Pruitt Realty</span><span>and Property</span><span>Management Services</span></div></div>
  </section>

  <section class="sheet envelope-front">
    <div class="brand"><span class="dot"></span><div class="words"><span>Pruitt Realty</span><span>and Property</span><span>Management Services</span></div></div>
  </section>

  <section class="sheet envelope-back">
    <svg class="band" viewBox="0 0 457 233" preserveAspectRatio="none" aria-hidden="true">
      <defs>
        <linearGradient id="envBlue" x1="0" x2="1"><stop offset="0" stop-color="#1f5d9c"/><stop offset="1" stop-color="#3d82c4"/></linearGradient>
      </defs>
      <rect x="0" y="40" width="457" height="80" fill="url(#envBlue)"/>
      <path d="M0 0 L457 0 L457 40 L0 40 Z" fill="#ffffff"/>
      <path d="M0 120 L228 200 L457 120 L457 233 L0 233 Z" fill="#ffffff"/>
      <path d="M0 120 L228 200 L457 120" fill="none" stroke="#d6dbe1" stroke-width="1.5"/>
    </svg>
    <div class="url">www.pruittrealty.example</div>
  </section>

</body>
</html>
```